velmora LED lighting Brochure design *

need a Brochure for velmora LED, that is a company specialises in industrial LED lighting solutions ... we also do retail, gas stations as well...
we are formed to serve customer need in lighting doing engineering, supply and installation of LED lighting
we need a Brochure that describe our company work, project cycle, project reference and services provided in addition to our main products that will be provided to consultant for product range approval

Target Market(s)

industrial sector (petrochemical, chemical, factories), construction, retail shops, gas stations

Industry/Entity Type

Lighting

Colors

Requirements
Must have
• project cycle
• project reference photos... cant upload it here

```html
<!DOCTYPE html>
<html lang="en">
<head>
<meta charset="utf-8">
<title>velmora LED lighting – Brochure</title>
<link href="https://fonts.googleapis.com/css2?family=Montserrat:wght@400;600;700;800&family=Open+Sans:wght@400;600&display=swap" rel="stylesheet">
<style>
:root{
  --backdrop:#e8e8e8;
  --paper:#ffffff;
  --navy:#1c2f4f;
  --orange:#f39a1e;
  --red:#e5412d;
  --sky:#2aa6d9;
  --green:#9cc53a;
  --grey-text:#5b6470;
  --rule:#e3e6ea;
  --stripe:#f4f6f8;
}
*{box-sizing:border-box;margin:0;padding:0}
html,body{width:849px;height:1200px;overflow:hidden;background:var(--backdrop)}
body{position:relative;font-family:"Open Sans",sans-serif;color:var(--navy)}
.spread{position:absolute;display:flex;box-shadow:0 6px 18px rgba(0,0,0,.15)}
.page{position:relative;background:var(--paper);flex:1;overflow:hidden}
.page + .page{border-left:1px solid #eee}

/* cover spread */
.cover-spread{left:85px;top:34px;width:685px;height:334px}
.brand{position:absolute;right:26px;top:28px;display:flex;align-items:center;gap:8px}
.brand-mark{width:14px;height:14px;background:var(--navy)}
.brand-name{font-family:"Montserrat",sans-serif;font-weight:700;font-size:13px;color:var(--navy);letter-spacing:.2px}
.dot-field{position:absolute;left:30px;top:80px;width:170px;height:254px;
  background:linear-gradient(135deg,var(--navy) 0%,#2d4a78 35%,var(--sky) 60%,var(--orange) 82%,var(--red) 100%);opacity:.9}
.tagline{position:absolute;right:16px;top:222px;text-align:right;font-family:"Montserrat",sans-serif;font-weight:800;font-size:8px;line-height:1.35;letter-spacing:.4px}
.tagline .accent{color:var(--orange)}
.tagline .dark{color:var(--navy)}

/* product spread */
.product-spread{left:51px;top:405px;width:750px;height:741px}
.product-photo{position:absolute;top:0;right:0}
.photo-flood{width:135px;height:200px;background:radial-gradient(circle at 60% 50%,#4a4f57 0%,#23272d 60%,#d9dde2 100%)}
.photo-highbay{width:170px;height:95px;background:radial-gradient(circle at 55% 45%,#c9ced4 0%,#3a3f46 55%,#e4e7ea 100%)}
.product-title{position:absolute;left:20px;top:70px;font-family:"Montserrat",sans-serif;font-weight:800;font-size:54px;line-height:.95;letter-spacing:-1px}
.title-flood{color:var(--orange)}
.title-highbay{color:var(--sky);top:112px;font-size:56px}
.intro{position:absolute;left:20px;top:228px;width:160px;font-size:7.5px;line-height:1.45;color:var(--grey-text)}
.area{position:absolute;left:20px;top:285px;width:170px;font-size:7px;color:var(--grey-text);line-height:1.4}
.area h3{font-family:"Montserrat",sans-serif;font-size:7.5px;font-weight:800;color:var(--navy);letter-spacing:.4px}
.spec-table{position:absolute;left:48px;top:310px;width:300px;border-collapse:collapse;font-size:6.8px}
.spec-table th{background:var(--navy);color:#fff;font-family:"Montserrat",sans-serif;font-weight:700;text-align:left;padding:5px 6px}
.spec-table td{padding:4.4px 6px;border-bottom:1px solid var(--rule);color:var(--grey-text)}
.spec-table tr:nth-child(even) td{background:var(--stripe)}
.spec-table td:first-child{color:var(--navy);font-weight:600;width:52%}
.highbay-page .spec-table{left:20px;top:330px}
.highbay-page .area{top:300px}
.highbay-page .intro{top:240px}
</style>
</head>
<body>

<section class="spread cover-spread">
  <div class="page back-cover"></div>
  <div class="page front-cover">
    <div class="brand"><span class="brand-mark"></span><span class="brand-name">velmora LED lighting</span></div>
    <div class="dot-field" role="img" aria-label="Grid of coloured dots in navy, orange, red, sky blue and green"></div>
    <p class="tagline"><span class="accent">ENGINEERING</span><br><span class="accent">LIGHTING SOLUTION</span><br><span class="dark">PROVIDER</span></p>
  </div>
</section>

<section class="spread product-spread">
  <div class="page flood-page">
    <div class="product-photo photo-flood" role="img" aria-label="Photo of an LED flood light fixture"></div>
    <h2 class="product-title title-flood">FLOOD<br>LIGHT</h2>
    <p class="intro">Velmora floodlights are designed for industrial lighting ensuring low energy use, long life and high light output.</p>
    <div class="area"><h3>AREA OF APPLICATION</h3><p>Factories, warehouses, yards, stadiums.</p></div>
    <table class="spec-table">
      <tr><th>MODEL</th><th>VFL-100</th></tr>
      <tr><td>Input Voltage</td><td>AC100-277V</td></tr>
      <tr><td>Frequency Range</td><td>50/60Hz</td></tr>
      <tr><td>Power Factor</td><td>&gt;0.95</td></tr>
      <tr><td>Power Efficiency</td><td>&gt;90%</td></tr>
      <tr><td>LED Chip</td><td>SMD 3030</td></tr>
      <tr><td>LED Luminous Efficiency</td><td>150 lm/W</td></tr>
      <tr><td>Light Output</td><td>15000 lm</td></tr>
      <tr><td>Available Beam Angle</td><td>60°/90°/120°</td></tr>
      <tr><td>Color Temperature</td><td>3000K-6500K</td></tr>
      <tr><td>Color Rendering Index</td><td>Ra&gt;80</td></tr>
      <tr><td>Light Distribution</td><td>Symmetric</td></tr>
      <tr><td>Working Temperature</td><td>-30~+50°C</td></tr>
      <tr><td>IP Grade</td><td>IP66</td></tr>
      <tr><td>Working Life Span</td><td>50000 hrs</td></tr>
      <tr><td>Certificate</td><td>CE, RoHS</td></tr>
    </table>
  </div>
  <div class="page highbay-page">
    <div class="product-photo photo-highbay" role="img" aria-label="Photo of a round LED highbay fixture"></div>
    <h2 class="product-title title-highbay">HIGHBAY</h2>
    <p class="intro">Velmora highbays are designed for industrial halls ensuring uniform light, low energy use and high efficiency.</p>
    <div class="area"><h3>AREA OF APPLICATION</h3><p>Warehouses, factories, halls, gas stations.</p></div>
    <table class="spec-table">
      <tr><th>MODEL</th><th>VHB-150</th></tr>
      <tr><td>Input Voltage</td><td>AC100-277V</td></tr>
      <tr><td>Frequency Range</td><td>50/60Hz</td></tr>
      <tr><td>Power Factor</td><td>&gt;0.95</td></tr>
      <tr><td>Power Efficiency</td><td>&gt;92%</td></tr>
      <tr><td>LED Chip</td><td>SMD 3030</td></tr>
      <tr><td>LED Luminous Efficiency</td><td>160 lm/W</td></tr>
      <tr><td>Light Output</td><td>24000 lm</td></tr>
      <tr><td>Available Beam Angle</td><td>60°/90°/120°</td></tr>
      <tr><td>Color Temperature</td><td>4000K-6500K</td></tr>
      <tr><td>Color Rendering Index</td><td>Ra&gt;80</td></tr>
      <tr><td>Light Distribution</td><td>Symmetric</td></tr>
      <tr><td>Working Temperature</td><td>-30~+50°C</td></tr>
      <tr><td>IP Grade</td><td>IP65</td></tr>
      <tr><td>Working Life Span</td><td>50000 hrs</td></tr>
      <tr><td>Certificate</td><td>CE, RoHS</td></tr>
    </table>
  </div>
</section>

</body>
</html>
```